Business Card Design

Buy and sell properties
Buy and rehab properties
Buy properties for cash
That is what I do but do need a logo
looking for some type of logo or design on it
Just started business
Back of card should say something like BUY HOUSES CASH
Overview: it is a new company. Basically I buy properties wholesale and fix them up and sell them or sell them to other fix and flippers
Background: company is new so not any background
Market: is basically anyone selling a house or buying a house. Someone that needs to sell house fast. Basically I am a cash home buyer!!!

Updates
Email on card should be:   harborlanerealtyinc@mailbox.test

Industry/Entity Type
House
Contact Information for Business Card
Harbor Lane Realty Inc
PO Box 718269
Cedar Marsh FL 32987

Dale Morrick
dmorrick@mailbox.test
555-271-6094

```html
<!DOCTYPE html>
<html lang="en">
<head>
<meta charset="utf-8">
<title>Harbor Lane Realty – Business Card</title>
<link rel="stylesheet" href="https://fonts.googleapis.com/css2?family=Oswald:wght@400;500;600&display=swap">
<style>
  :root {
    --green: #8dc63f;
    --green-text: #7cb82f;
    --ink: #3b3b3b;
    --paper: #ffffff;
    --canvas: #ffffff;
    --shadow: rgba(0, 0, 0, 0.28);
  }
  * { box-sizing: border-box; margin: 0; padding: 0; }
  html, body {
    width: 1200px; height: 1200px; overflow: hidden;
    background: var(--canvas);
    font-family: "Oswald", "Arial Narrow", sans-serif;
  }
  .stage { position: relative; width: 1200px; height: 1200px; }

  .card {
    position: absolute;
    background: var(--paper);
    box-shadow: 4px 6px 14px var(--shadow);
    overflow: hidden;
  }
  .card--front { left: 204px; top: 84px; width: 954px; height: 471px; }
  .card--back  { left: 246px; top: 600px; width: 909px; height: 465px; }

  .front__band {
    position: absolute; left: 186px; top: 0;
    width: 426px; height: 100%;
    background: var(--green);
  }
  .back__band {
    position: absolute; left: 0; top: 0;
    width: 354px; height: 100%;
    background: var(--green);
  }

  .brand-mark {
    position: absolute;
    background: var(--paper);
    display: flex; flex-direction: column;
    align-items: center; justify-content: center;
    color: var(--ink);
    font-weight: 600;
    text-align: center;
    line-height: 1.08;
  }
  .card--front .brand-mark {
    left: 51px; top: 36px; width: 324px; height: 324px;
    font-size: 50px;
  }
  .card--back .brand-mark {
    left: 21px; top: 66px; width: 294px; height: 294px;
    font-size: 45px;
  }

  .front__tagline {
    position: absolute; left: 0; right: 0; top: 394px;
    text-align: center;
    color: var(--paper);
    font-weight: 500;
    font-size: 34px;
    letter-spacing: 2px;
  }

  .contact {
    position: absolute; left: 384px; top: 102px;
    color: var(--ink);
  }
  .contact__name,
  .contact__company {
    color: var(--green-text);
    font-weight: 500;
    font-size: 30px;
    line-height: 1.2;
  }
  .contact__line {
    font-size: 17px;
    line-height: 26px;
    font-weight: 400;
    white-space: nowrap;
  }
  .contact__phone { display: flex; align-items: center; gap: 7px; }
  .contact__phone svg { width: 16px; height: 16px; }
  .contact__company { margin-top: 34px; }
  .contact__address { margin-top: 6px; }
</style>
</head>
<body>
<main class="stage">

  <section class="card card--front" aria-label="Card front">
    <div class="front__band">
      <div class="brand-mark"><span>Harbor Lane</span><span>Realty</span></div>
      <p class="front__tagline">BUY HOUSES CASH</p>
    </div>
  </section>

  <section class="card card--back" aria-label="Card back">
    <div class="back__band">
      <div class="brand-mark"><span>Harbor Lane</span><span>Realty</span></div>
    </div>
    <div class="contact">
      <p class="contact__name">Dale Morrick</p>
      <p class="contact__line">harborlanerealtyinc@mailbox.test</p>
      <p class="contact__line contact__phone">
        <svg viewBox="0 0 24 24" aria-hidden="true"><path fill="none" stroke="#3b3b3b" stroke-width="2" stroke-linejoin="round" d="M6.6 2.5l3 3.6-2 2.4a13 13 0 0 0 7.9 7.9l2.4-2 3.6 3-2 3.1C12.4 21 3 11.6 3.5 4.5z"/></svg>
        555-271-6094
      </p>
      <p class="contact__company">Harbor Lane Realty Inc</p>
      <div class="contact__address">
        <p class="contact__line">PO Box 718269</p>
        <p class="contact__line">Cedar Marsh</p>
        <p class="contact__line">FL 32987</p>
      </div>
    </div>
  </section>

</main>
</body>
</html>
```